Vesit cards for web development company

We need a business card design for our company. The company develops online platforms and conducts marketing consulting. Company logo. The cards must fit in with us (a junior start UP), but they must also be professional enough to impress with investors like banks. We wish you a combination of classic and modern design

Target Market(s)

Business partners and IT and marketing customers

Industry/Entity Type

It Company

Contact Information for Business Card

Folgende Information müssen Drauf.
Name, Position, Telefon Nr., Mobile Nr., E-Mail adresse, Optional sind noch Webadresse und HRB Nummer

Colors

Designer to choose colors to be used in the design.

Requirements
Must have
• The cards have to fit into the logo later and have to be dynamic and serious at the same time

```html
<!DOCTYPE html>
<html lang="en">
<head>
<meta charset="UTF-8">
<title>Arvento Labs – Business Card</title>
<link href="https://fonts.googleapis.com/css2?family=Open+Sans:wght@400;600;700&display=swap" rel="stylesheet">
<style>
  :root {
    --stage: #000000;
    --card-blue: #0f75bc;
    --card-grey: #939598;
    --ink-light: #ffffff;
    --ink-blue: #1877c0;
  }
  * { margin: 0; padding: 0; box-sizing: border-box; }
  html, body { width: 1200px; height: 900px; overflow: hidden; background: var(--stage); }
  body { position: relative; font-family: "Open Sans", Arial, sans-serif; }

  .card { position: absolute; top: 275px; width: 477px; height: 293px; }
  .card-front {
    left: 116px; background: var(--card-blue); color: var(--ink-light);
    border-radius: 0 52px 0 52px;
  }
  .card-back {
    left: 622px; top: 276px; height: 292px; background: var(--card-grey);
    border-radius: 52px 0 52px 0;
  }

  .holder { position: absolute; left: 22px; top: 31px; }
  .holder-name { font-size: 16.5px; font-weight: 700; line-height: 1.1; }
  .holder-role { font-size: 12.5px; margin-top: 2px; }
  .address { position: absolute; left: 22px; top: 85px; font-size: 12.5px; line-height: 15px; }

  .contacts { position: absolute; right: 26px; top: 40px; list-style: none; text-align: right; }
  .contacts li {
    font-size: 12.5px; height: 19.7px; display: flex; align-items: center; justify-content: flex-end; gap: 8px;
  }
  .contacts svg { width: 10px; height: 10px; fill: var(--ink-light); }

  .brand {
    position: absolute; left: 0; right: 0; display: flex; align-items: center; justify-content: center;
    gap: 10px; font-weight: 700; letter-spacing: 1px; text-transform: uppercase;
  }
  .card-front .brand { top: 200px; font-size: 30px; color: var(--ink-light); }
  .card-front .brand-dot { background: var(--ink-light); }
  .card-back .brand { top: 158px; font-size: 30px; color: var(--ink-blue); }
  .card-back .brand-dot { background: var(--ink-blue); }
  .brand-dot { width: 18px; height: 18px; border-radius: 50%; }
</style>
</head>
<body>
  <section class="card card-front">
    <div class="holder">
      <p class="holder-name">Jonathan Smith</p>
      <p class="holder-role">Managing Director</p>
    </div>
    <p class="address">12345, Address Goes Here<br>Country Name, 123456</p>
    <ul class="contacts">
      <li>(044)-456-7890
        <svg viewBox="0 0 10 10"><path d="M2 0.5 L3.6 2.6 L2.8 3.6 Q4 6 6.4 7.2 L7.4 6.4 L9.5 8 L8.4 9.5 Q3.5 9 0.5 1.6 Z"/></svg></li>
      <li>123-456-7890
        <svg viewBox="0 0 10 10"><path d="M1 0.5h8v9h-8z M2.2 1.7v6.6h5.6v-6.6z" fill-rule="evenodd"/></svg></li>
      <li>info@youremail.com
        <svg viewBox="0 0 10 10"><path d="M0.5 2h9v6h-9z M1.3 2.6 L5 5.4 L8.7 2.6" fill-rule="evenodd"/><path d="M1 2.6 L5 5.6 L9 2.6" stroke="#0f75bc" stroke-width="0.9" fill="none"/></svg></li>
      <li>www.website.com
        <svg viewBox="0 0 10 10"><circle cx="5" cy="5" r="4.6"/><path d="M2.5 3 Q4 3.5 4 5 T3 8 M6 1.5 Q5.5 3 7 3.8 T8.5 6" stroke="#0f75bc" stroke-width="0.9" fill="none"/></svg></li>
    </ul>
    <div class="brand"><span class="brand-dot"></span>Arvento Labs</div>
  </section>

  <section class="card card-back">
    <div class="brand"><span class="brand-dot"></span>Arvento Labs</div>
  </section>
</body>
</html>
```